Flyer für Anbieter von Gruppenritualen
Zielgruppe
Wir sind zwei Frauen (1x Yogalehrerin & Kalivento Therapeutin, 1x Ritualfachfrau), die regelmässig (aktuell 4x pro Jahr) Gruppenrituale anbieten. Unsere Zielgruppe sind vor allem Frauen (aber nicht ausschliesslich) jeglichen Alters, die sich etwas Schönes gönnen im Alltag.
Aufgabenstellung
Das Design soll ästhetisch schön und durchdacht sein. Ich schicke den Flyer mit, wie wir ihn bisher verwendet haben. Wir wünschen uns nun ein leichteres und stimmigeres Erscheinungsbild.
Praktisch wäre Format A5 oder 1:1.
Der Flyer soll die folgenden Elemente enthalten:
- Übersicht der 4 Daten + Veranstaltungsthemen
- Beschrieb, was eine Licht-Hain (so nennen sich unsere Gruppenrituale) ist
- ggf. Beschrieb vom Leitungsteam
Bei der Auswahl wird sicher auch eine Rolle spielen, ob das Design sich eignet zum Übertragen für die Ausschreibung der Einzelnenanlässe. Dazu schicke ich auch Beispiele, wie wir das letztes Jahr gemacht haben. Diese können auch als Inspiration für diesen Flyer dienen.
Konkrete Texte finden sich in einer Worddatei im Anhang zum Rauskopieren.

```html
<!DOCTYPE html>
<html lang="de">
<head>
<meta charset="utf-8">
<title>Licht-Hain – Flyer</title>
<link href="https://fonts.googleapis.com/css2?family=Righteous&family=Poppins:wght@400;600;700&display=swap" rel="stylesheet">
<style>
  :root{
    --backdrop:#e6e6e6;
    --paper:#ffffff;
    --royal:#223a98;
    --royal-deep:#1a2f82;
    --gold:#c9a227;
    --green:#0b8a3c;
    --ink:#1b1b1b;
    --red:#d11f2a;
    --panel:#eceef0;
  }
  *{box-sizing:border-box;margin:0;padding:0}
  html,body{width:1200px;height:1117px;overflow:hidden;background:var(--backdrop)}
  body{font-family:"Poppins",sans-serif;color:var(--ink);position:relative}

  .flyer{position:absolute;left:219px;top:20px;width:762px;height:1077px;background:var(--paper);overflow:hidden;box-shadow:0 6px 24px rgba(0,0,0,.15)}
  .hero-band{position:absolute;left:0;top:0;width:762px;height:520px}

  .title{position:absolute;left:0;right:0;top:30px;text-align:center;font-family:"Righteous",sans-serif;font-weight:400;font-size:104px;line-height:1.1;color:#fff;letter-spacing:2px}
  .intro{position:absolute;left:48px;right:40px;top:160px;color:#fff;font-weight:600;font-size:12.6px;line-height:1.5}

  .program{position:absolute;left:40px;top:300px;width:682px;height:470px;background:var(--paper);border:2px solid var(--royal)}
  .dates{position:absolute;top:26px;width:300px;font-size:12.6px;line-height:1.42;list-style:none}
  .dates--full{left:30px}
  .dates--short{left:350px;top:12px}
  .dates__note{font-weight:700;font-style:italic;font-size:12px;margin-bottom:2px}
  .dates li{position:relative;padding-left:20px}
  .dates li svg{position:absolute;left:0;top:3px;width:12px;height:12px}
  .dates b{font-weight:700}

  .color-strip{position:absolute;left:26px;right:26px;top:200px;height:244px;display:flex}
  .color-strip span{flex:1}
  .swatch-green{background:linear-gradient(#0b9a45 0%,#0a8a3c 45%,#064a22 60%,#0a7a35 100%)}
  .swatch-blue{background:linear-gradient(#1e3596 0%,#1a2e88 45%,#0f1c5e 58%,#2a5ab8 75%,#122266 100%)}
  .swatch-yellow{background:linear-gradient(#e7c33a 0%,#e4bd2a 45%,#b98a1f 60%,#c9981f 100%)}
  .swatch-red{background:linear-gradient(#d71f28 0%,#d41c26 45%,#b0141d 58%,#e2222b 100%)}

  .team__heading{position:absolute;left:40px;top:784px;font-weight:700;font-size:20px;line-height:1.4;color:var(--royal)}
  .team{position:absolute;left:26px;right:26px;top:814px;height:110px;background:var(--panel);display:flex;align-items:center}
  .member{flex:1;display:flex;align-items:center;gap:16px;padding:0 22px;font-size:12.6px;line-height:1.35}
  .member + .member{border-left:2px solid #fff}
  .member__portrait{flex:none;width:80px;height:80px;border-radius:50%;background:radial-gradient(circle at 50% 40%,#bdbdbd,#6e6e6e)}
  .member__name{font-weight:700}

  .info{position:absolute;left:40px;right:40px;top:938px}
  .info__heading{display:flex;align-items:center;gap:14px;font-weight:700;font-size:20px;line-height:1.4;color:var(--green);margin-bottom:4px}
  .info__heading::after{content:"";flex:1;height:2px;background:var(--green)}
  .info p{font-size:12.6px;line-height:1.4}
  .info b{font-weight:700}
</style>
</head>
<body>
<main class="flyer">
  <svg class="hero-band" viewBox="0 0 762 520" aria-hidden="true">
    <path d="M0 0H762V500Q381 380 0 440Z" fill="var(--royal)"/>
    <path d="M0 440Q381 380 762 500" fill="none" stroke="var(--gold)" stroke-width="14"/>
    <path d="M0 0H762V300H0Z" fill="var(--royal-deep)" opacity=".25"/>
  </svg>

  <h1 class="title">Licht-Hain</h1>
  <p class="intro">In der Licht-Hain widmen wir uns einer Farbe und Themen, die mit dieser Farbe verknüpft sind. Genau wie die Oase in der Wüste ist die Licht-Hain ein Ort zum Auftanken, Entspannen und sich Nähren. In der Gruppe tauchen wir tief ins Thema ein mit Achtsamkeitsübungen, Kalivento®, Bewegung, kreativen Momenten und Gruppenritualen. Die Licht-Haine können einzeln oder als 4-teiligen Anlass besucht werden.</p>

  <section class="program">
    <ul class="dates dates--full">
      <li><svg viewBox="0 0 12 12"><circle cx="6" cy="6" r="6" fill="var(--gold)"/><path d="M3.3 6.2l1.8 1.7 3.6-3.6" stroke="#fff" stroke-width="1.6" fill="none"/></svg><b>ROT:</b> «Geerdet für sich einstehen»<br>Donnerstag, 20. März 2025</li>
      <li><svg viewBox="0 0 12 12"><circle cx="6" cy="6" r="6" fill="var(--gold)"/><path d="M3.3 6.2l1.8 1.7 3.6-3.6" stroke="#fff" stroke-width="1.6" fill="none"/></svg><b>BLAU:</b> «Sich nähren und in Fülle sein»<br>Dienstag, 17. Juni 2025</li>
      <li><svg viewBox="0 0 12 12"><circle cx="6" cy="6" r="6" fill="var(--gold)"/><path d="M3.3 6.2l1.8 1.7 3.6-3.6" stroke="#fff" stroke-width="1.6" fill="none"/></svg><b>GELB:</b> «Dankbar ernten»<br>Montag, 20. Oktober 2025</li>
      <li><svg viewBox="0 0 12 12"><circle cx="6" cy="6" r="6" fill="var(--gold)"/><path d="M3.3 6.2l1.8 1.7 3.6-3.6" stroke="#fff" stroke-width="1.6" fill="none"/></svg><b>GRÜN:</b> «Ausgeglichen auf dem Herzensweg»<br>Donnerstag, 4. Dezember 2024</li>
    </ul>
    <ul class="dates dates--short">
      <p class="dates__note">Alternative mit weniger Zeichen</p>
      <li><svg viewBox="0 0 12 12"><circle cx="6" cy="6" r="6" fill="var(--red)"/><path d="M3.3 6.2l1.8 1.7 3.6-3.6" stroke="#fff" stroke-width="1.6" fill="none"/></svg><b>ROT:</b> «Geerdet für sich einstehen»<br>Do, 20. März 2025</li>
      <li><svg viewBox="0 0 12 12"><circle cx="6" cy="6" r="6" fill="var(--red)"/><path d="M3.3 6.2l1.8 1.7 3.6-3.6" stroke="#fff" stroke-width="1.6" fill="none"/></svg><b>BLAU:</b> «Sich nähren und in Fülle sein»<br>Di, 17. Juni 2025</li>
      <li><svg viewBox="0 0 12 12"><circle cx="6" cy="6" r="6" fill="var(--red)"/><path d="M3.3 6.2l1.8 1.7 3.6-3.6" stroke="#fff" stroke-width="1.6" fill="none"/></svg><b>GELB:</b> «Dankbar ernten»<br>Mo, 20. Oktober 2025</li>
      <li><svg viewBox="0 0 12 12"><circle cx="6" cy="6" r="6" fill="var(--red)"/><path d="M3.3 6.2l1.8 1.7 3.6-3.6" stroke="#fff" stroke-width="1.6" fill="none"/></svg><b>GRÜN:</b> «Ausgeglichen auf dem Herzensweg»<br>Do, 4. Dezember 2024</li>
    </ul>
    <div class="color-strip" role="img" aria-label="Foto: vier Glasflaschen mit grüner, blauer, gelber und roter Flüssigkeit nebeneinander">
      <span class="swatch-green"></span><span class="swatch-blue"></span><span class="swatch-yellow"></span><span class="swatch-red"></span>
    </div>
  </section>

  <h2 class="team__heading">Leitungsteam</h2>
  <section class="team">
    <div class="member">
      <div class="member__portrait" role="img" aria-label="Porträtfoto von Selina Varga"></div>
      <p><span class="member__name">Selina Varga,</span><br>Kalivento® practitioner,<br>Yoga- und Achtsamkeitslehrerin<br>selina-varga.ch</p>
    </div>
    <div class="member">
      <div class="member__portrait" role="img" aria-label="Porträtfoto von Andrea Lüthi"></div>
      <p><span class="member__name">Andrea Lüthi,</span><br>Fachfrau für Rituale und<br>Fotografin andrealuethi.ch</p>
    </div>
  </section>

  <section class="info">
    <h2 class="info__heading">Mehr Informationen</h2>
    <p><b>Zeit:</b> 18:45–21:00 Uhr</p>
    <p><b>Ort:</b> Zwischenraum, Raum 113, Lindenweg 12, 3012 Bern</p>
    <p><b>Anmeldung:</b> erforderlich via andrealuethi.ch oder selina-varga.ch</p>
    <p><b>Kosten:</b> CHF 50.–, reduziert, wenn mehrere Licht-Haine besucht werden. Solipreise möglich.</p>
  </section>
</main>
</body>
</html>
```